BrackenfieldGoods.com

I need a site that I can sell dewatering equipment to the construction industry.
Ie, pipes fittings pumps and other such things needed to remove the groundwater on construction sites. Here in Florida, it’s needed almost everywhere seeing we are at sea level.
I want to be able to sell these products on the site and receive

Coding

Coded - Design and coding required

Number of Pages Required

1 page

```html
<!DOCTYPE html>
<html lang="en">
<head>
<meta charset="utf-8">
<title>BrackenfieldGoods.com</title>
<link href="https://fonts.googleapis.com/css2?family=Exo+2:wght@500;600;700&family=Source+Sans+3:ital,wght@0,400;0,600;0,700;1,600;1,700&display=swap" rel="stylesheet">
<style>
:root{
  --blue:#0b5f96;
  --blue-dark:#084a75;
  --blue-deep:#063a5c;
  --green:#1db43c;
  --ink:#2b2b2b;
  --muted:#5d5d5d;
  --line:#cfcfcf;
  --card:#f3f3f3;
  --white:#ffffff;
}
*{box-sizing:border-box;margin:0;padding:0}
html,body{width:1200px;height:2542px;overflow:hidden;background:var(--white)}
body{position:relative;font-family:"Source Sans 3",Arial,sans-serif;color:var(--ink)}
.brand{font-family:"Exo 2",Arial,sans-serif;font-weight:600;color:var(--blue);letter-spacing:.3px}

/* header */
.site-header{position:absolute;left:0;top:0;width:1200px;height:129px;background:var(--white)}
.utility-bar{position:absolute;right:0;top:0;width:670px;height:46px;background:var(--blue);
  clip-path:polygon(0 0,100% 0,100% 100%,40px 100%);display:flex;align-items:center;justify-content:flex-end;gap:26px;padding-right:26px;
  color:var(--white);font-size:14px;font-weight:700;letter-spacing:.4px;text-transform:uppercase}
.utility-bar span{display:flex;align-items:center;gap:7px}
.phone-pill{background:var(--green);border:2px solid #bff0c9;border-radius:14px;padding:3px 22px;margin-right:10px;font-size:14px;text-transform:none}
.utility-bar svg{width:14px;height:14px;fill:none;stroke:var(--white);stroke-width:2}
.site-header .brand{position:absolute;left:44px;top:60px;font-size:25px}
.main-nav{position:absolute;right:28px;top:82px;display:flex;align-items:center;gap:30px;font-size:14px;font-weight:700;color:#555;text-transform:uppercase;letter-spacing:.3px}
.main-nav span{display:flex;align-items:center;gap:6px}
.main-nav svg{width:15px;height:15px;fill:none;stroke:#666;stroke-width:2}
.nav-home{width:38px;height:28px;background:var(--blue);display:flex;align-items:center;justify-content:center}
.nav-home svg{stroke:none;fill:var(--white)}

/* hero */
.hero{position:absolute;left:0;top:129px;width:1200px;height:556px;
  background:linear-gradient(180deg,#8e9296 0%,#a7a5a0 45%,#b98f6f 70%,#6f5a52 100%);
  display:flex;flex-direction:column;align-items:center;justify-content:center;padding-top:10px}
.hero h1{font-size:41px;font-weight:700;color:var(--white);letter-spacing:.6px;text-shadow:0 2px 4px rgba(0,0,0,.55);margin-top:40px}
.hero .btn{margin-top:18px;width:222px;height:52px;background:var(--blue);border:2px solid #b9d6ea;color:var(--white);
  font-size:19px;font-weight:700;letter-spacing:1px;display:flex;align-items:center;justify-content:center}

/* products */
.products{position:absolute;left:0;top:685px;width:1200px;height:944px}
.section-title{font-family:"Exo 2",Arial,sans-serif;font-weight:600;font-size:22px;letter-spacing:1.5px;text-align:center}
.products .section-title{position:absolute;left:0;right:0;top:100px;color:var(--ink)}
.category-list{position:absolute;left:64px;top:175px;width:280px;height:415px;border-right:2px solid var(--blue);list-style:none}
.category-list li{height:48px;margin-bottom:8px;background:var(--blue);color:var(--white);font-size:15px;font-weight:700;
  display:flex;align-items:center;padding-left:26px;border-radius:4px 0 0 4px}
.category-list li.active{background:var(--white);color:var(--ink);border:2px solid var(--blue);border-right:none;margin-top:-6px}
.product-grid{position:absolute;left:398px;top:165px;display:grid;grid-template-columns:repeat(3,238px);column-gap:12px;row-gap:34px}
.product-card{width:238px}
.product-photo{height:190px;border-radius:2px}
.product-photo.red{background:radial-gradient(ellipse at 50% 55%,#d8262b 0%,#b81d22 40%,#ffffff 72%)}
.product-photo.blue{background:radial-gradient(ellipse at 50% 50%,#2b55c8 0%,#1f3f9c 40%,#ffffff 72%)}
.product-info{margin-top:8px;height:128px;background:var(--card);box-shadow:0 4px 6px rgba(0,0,0,.12);padding:18px 16px 0}
.product-info h3{font-size:16px;font-weight:700;line-height:21px;color:var(--ink);padding-bottom:10px;border-bottom:1px solid var(--line)}
.price-row{display:flex;align-items:center;justify-content:space-between;margin-top:14px;font-size:17px;font-weight:700}
.price{display:flex;align-items:center;gap:8px}
.dollar{width:22px;height:22px;border:2px solid var(--ink);border-radius:50%;font-size:13px;display:flex;align-items:center;justify-content:center}
.price-row svg{width:24px;height:22px;fill:none;stroke:var(--ink);stroke-width:2}

/* testimonials */
.testimonials{position:absolute;left:0;top:1629px;width:1200px;height:483px;
  background:linear-gradient(180deg,#0f78b3 0%,#0a5f93 55%,#074d79 100%)}
.testimonials .section-title{position:absolute;left:0;right:0;top:90px;color:var(--white)}
.quote{position:absolute;top:166px;width:323px;height:174px;border:2px solid rgba(255,255,255,.85);border-radius:8px;
  background:rgba(3,40,66,.35);padding:20px 22px 0 56px;color:var(--white);font-size:15.5px;line-height:21px}
.quote::before{content:"\201C";position:absolute;left:14px;top:2px;font-size:58px;font-weight:700;line-height:58px;font-family:Georgia,serif}
.quote .close{font-family:Georgia,serif;font-size:40px;font-weight:700;line-height:10px;vertical-align:-14px;margin-left:6px}
.quote .tail{position:absolute;left:44px;bottom:-16px;width:28px;height:16px;background:#0a5686;clip-path:polygon(0 0,100% 0,0 100%)}
.quote .tail-line{position:absolute;left:42px;bottom:-18px;width:32px;height:18px;border-left:2px solid rgba(255,255,255,.85);transform-origin:0 0}
.avatar{position:absolute;right:-8px;bottom:-48px;width:95px;height:95px;border-radius:50%;border:3px solid var(--white);background:#d9c8bb}
.reviewer{position:absolute;top:364px;color:var(--white);font-size:17px;font-weight:700;font-style:italic}

/* footer */
.site-footer{position:absolute;left:0;top:2112px;width:1200px;height:430px}
.site-footer .brand{position:absolute;left:0;right:0;top:56px;text-align:center;font-size:23px}
.footer-col{position:absolute;top:135px}
.footer-col h4{font-size:15px;font-weight:700;color:#444;letter-spacing:.3px;text-transform:uppercase;padding-bottom:10px;border-bottom:1px solid var(--line);margin-bottom:12px}
.footer-col p,.footer-col li{font-size:13px;line-height:19px;color:var(--muted);font-weight:600}
.footer-col ul{list-style:none}
.contact-row{display:flex;gap:8px;margin-bottom:14px;font-size:13px;line-height:19px;color:var(--muted);font-weight:600}
.contact-row svg{flex:none;width:17px;height:17px;fill:none;stroke:#555;stroke-width:1.8;margin-top:1px}
.social-row{display:flex;align-items:center;gap:12px;margin-bottom:12px;font-size:13px;color:var(--muted);font-weight:600}
.social-dot{width:20px;height:20px;border-radius:50%;background:var(--blue)}
.copyright{position:absolute;left:0;bottom:0;width:1200px;height:40px;background:var(--blue);color:var(--white);
  font-size:12px;font-weight:700;letter-spacing:.5px;display:flex;align-items:center;justify-content:center}
</style>
</head>
<body>

<header class="site-header">
  <div class="utility-bar">
    <span class="phone-pill">
      <svg viewBox="0 0 16 16"><path d="M3 2l3 0 1 3-2 1.5a9 9 0 0 0 4.5 4.5L11 9l3 1v3c0 1-1 1.5-2 1.5A11 11 0 0 1 1.5 4C1.5 3 2 2 3 2z" fill="#fff" stroke="none"/></svg>1800.555.0148
    </span>
    <span><svg viewBox="0 0 16 16"><circle cx="8" cy="5" r="3"/><path d="M2 15c0-4 3-5.5 6-5.5s6 1.5 6 5.5"/></svg>Login</span>
    <span><svg viewBox="0 0 16 16"><circle cx="8" cy="8" r="6.5"/><path d="M8 5v6M5 8h6"/></svg>Register</span>
    <span><svg viewBox="0 0 16 16"><path d="M1 2h2l2 8h8l2-6H4"/><circle cx="6" cy="13" r="1"/><circle cx="12" cy="13" r="1"/></svg>Cart</span>
    <span><svg viewBox="0 0 16 16"><circle cx="7" cy="7" r="4.5"/><path d="M10.5 10.5L15 15"/></svg>Search</span>
  </div>
  <div class="brand">BrackenfieldGoods.com</div>
  <nav class="main-nav">
    <span class="nav-home"><svg viewBox="0 0 16 16"><path d="M8 1.5L1 8h2v6h4v-4h2v4h4V8h2z"/></svg></span>
    <span><svg viewBox="0 0 16 16"><path d="M3 3v7h10M10 7l3 3-3 3"/></svg>Products</span>
    <span><svg viewBox="0 0 16 16"><rect x="2" y="6" width="12" height="8"/><path d="M1 6l2-4h10l2 4"/></svg>Shop</span>
    <span><svg viewBox="0 0 16 16"><path d="M2 3h12v8H7l-3 3v-3H2z"/></svg>Testimonials</span>
    <span><svg viewBox="0 0 16 16"><path d="M2 3h12v7H9l-3 3V10H2z" fill="#666"/></svg>About</span>
    <span><svg viewBox="0 0 16 16"><rect x="1.5" y="3.5" width="13" height="9"/><path d="M1.5 3.5L8 9l6.5-5.5"/></svg>Contact</span>
  </nav>
</header>

<section class="hero" role="img" aria-label="Photo of water gushing from a large discharge pipe against a sunset sky">
  <h1>THE LEADING SUPPLIER FOR DEWATERING INDUSTRY</h1>
  <div class="btn">SHOP NOW</div>
</section>

<section class="products">
  <h2 class="section-title">PRODUCTS</h2>
  <ul class="category-list">
    <li class="active">Well Point Pumps</li>
    <li>Jet Pumps</li>
    <li>Hydraulic Pumps</li>
    <li>Header Pipe</li>
    <li>Header Pipe Plug</li>
    <li>Self Jet Dewatering</li>
    <li>Accessories</li>
  </ul>
  <div class="product-grid">
    <article class="product-card"><div class="product-photo red" role="img" aria-label="Red skid-mounted well point pump"></div>
      <div class="product-info"><h3>Well Point Pump<br>AB - 100</h3><div class="price-row"><span class="price"><span class="dollar">$</span>1545.00</span><svg viewBox="0 0 24 22"><path d="M1 2h4l3 12h12l3-9H6"/><circle cx="10" cy="18" r="1.6"/><circle cx="18" cy="18" r="1.6"/></svg></div></div></article>
    <article class="product-card"><div class="product-photo blue" role="img" aria-label="Blue skid-mounted well point pump"></div>
      <div class="product-info"><h3>Well Point Pump<br>AB - 101</h3><div class="price-row"><span class="price"><span class="dollar">$</span>2485.00</span><svg viewBox="0 0 24 22"><path d="M1 2h4l3 12h12l3-9H6"/><circle cx="10" cy="18" r="1.6"/><circle cx="18" cy="18" r="1.6"/></svg></div></div></article>
    <article class="product-card"><div class="product-photo red" role="img" aria-label="Red skid-mounted well point pump"></div>
      <div class="product-info"><h3>Well Point Pump<br>AB - 102</h3><div class="price-row"><span class="price"><span class="dollar">$</span>1585.00</span><svg viewBox="0 0 24 22"><path d="M1 2h4l3 12h12l3-9H6"/><circle cx="10" cy="18" r="1.6"/><circle cx="18" cy="18" r="1.6"/></svg></div></div></article>
    <article class="product-card"><div class="product-photo red" role="img" aria-label="Red skid-mounted well point pump"></div>
      <div class="product-info"><h3>Well Point Pump<br>AB - 100</h3><div class="price-row"><span class="price"><span class="dollar">$</span>1545.00</span><svg viewBox="0 0 24 22"><path d="M1 2h4l3 12h12l3-9H6"/><circle cx="10" cy="18" r="1.6"/><circle cx="18" cy="18" r="1.6"/></svg></div></div></article>
    <article class="product-card"><div class="product-photo blue" role="img" aria-label="Blue skid-mounted well point pump"></div>
      <div class="product-info"><h3>Well Point Pump<br>AB - 101</h3><div class="price-row"><span class="price"><span class="dollar">$</span>2485.00</span><svg viewBox="0 0 24 22"><path d="M1 2h4l3 12h12l3-9H6"/><circle cx="10" cy="18" r="1.6"/><circle cx="18" cy="18" r="1.6"/></svg></div></div></article>
    <article class="product-card"><div class="product-photo red" role="img" aria-label="Red skid-mounted well point pump"></div>
      <div class="product-info"><h3>Well Point Pump<br>AB - 102</h3><div class="price-row"><span class="price"><span class="dollar">$</span>1585.00</span><svg viewBox="0 0 24 22"><path d="M1 2h4l3 12h12l3-9H6"/><circle cx="10" cy="18" r="1.6"/><circle cx="18" cy="18" r="1.6"/></svg></div></div></article>
  </div>
</section>

<section class="testimonials" role="img" aria-label="Blue-tinted background photo of industrial pipe fittings">
  <h2 class="section-title">TESTIMONIALS</h2>
  <blockquote class="quote" style="left:88px">Lorem ipsum dolor sit amet, consect er adipiscing elit, sed diam nonummy nibh euismod tincidunt ut laoreet do magna aliquam erat volu. Wisi enim minim veniam.<span class="close">&#8221;</span>
    <span class="tail"></span><span class="avatar" role="img" aria-label="Customer portrait"></span></blockquote>
  <blockquote class="quote" style="left:439px">Lorem ipsum dolor sit amet, consect er adipiscing elit, sed diam nonummy nibh euismod tincidunt ut laoreet do magna aliquam erat volu. Wisi enim minim veniam.<span class="close">&#8221;</span>
    <span class="tail"></span><span class="avatar" role="img" aria-label="Customer portrait" style="background:#e6d3c2"></span></blockquote>
  <blockquote class="quote" style="left:790px">Lorem ipsum dolor sit amet, consect er adipiscing elit, sed diam nonummy nibh euismod tincidunt ut laoreet do magna aliquam erat volu. Wisi enim minim veniam.<span class="close">&#8221;</span>
    <span class="tail"></span><span class="avatar" role="img" aria-label="Customer portrait" style="background:#cdb9a8"></span></blockquote>
  <p class="reviewer" style="left:90px">Marisol Penhale</p>
  <p class="reviewer" style="left:441px">Dara Quillon</p>
  <p class="reviewer" style="left:792px">Theo Ashgrove</p>
</section>

<footer class="site-footer">
  <div class="brand">BrackenfieldGoods.com</div>
  <div class="footer-col" style="left:61px;width:304px">
    <h4>About Us</h4>
    <p>Lorem ipsum dolor sit amet, consectetur adipiscing elit, sed do eiusmod tempor incididunt ut labore et dolore magna aliqua. Ut enim ad minim veniam, qui nostrud exercitation ullamco laboris nisi ut aliquip ex ea commodo consequat. Duis aute irure dolor in reprehender it in voluptate velit esse cillum dolore eu fugiat nulla pariatur.</p>
  </div>
  <div class="footer-col" style="left:432px;width:100px">
    <h4>Quick Links</h4>
    <ul><li>Home</li><li>Products</li><li>Shop</li><li>Testimonials</li><li>About</li><li>Contact</li></ul>
  </div>
  <div class="footer-col" style="left:597px;width:115px">
    <h4>Information</h4>
    <ul><li>FAQs</li><li>Terms &amp; Conditions</li><li>Shipping</li><li>Return Policy</li></ul>
  </div>
  <div class="footer-col" style="left:781px;width:195px">
    <h4>Contact</h4>
    <div class="contact-row"><svg viewBox="0 0 16 16"><path d="M8 15s5-5 5-9A5 5 0 0 0 3 6c0 4 5 9 5 9z"/><circle cx="8" cy="6" r="1.8"/></svg><span>BrackenfieldGoods.com<br>48 Marlow Quay Road<br>Harborview, FL 33010</span></div>
    <div class="contact-row"><svg viewBox="0 0 16 16"><circle cx="8" cy="8" r="7"/><path d="M5.5 4.5h1.5l.7 2-1 .8a5 5 0 0 0 2 2l.8-1 2 .7v1.5c0 .5-.5.8-1 .8A6 6 0 0 1 4.7 5.3c0-.5.3-.8.8-.8z"/></svg><span>1800.555.0148</span></div>
    <div class="contact-row"><svg viewBox="0 0 16 16"><circle cx="8" cy="8" r="7"/><rect x="4.5" y="5.5" width="7" height="5"/><path d="M4.5 5.5L8 8.5l3.5-3"/></svg><span>info@brackenfieldgoods.com</span></div>
  </div>
  <div class="footer-col" style="left:1041px;width:100px">
    <h4>Follow Us</h4>
    <div class="social-row"><span class="social-dot"></span>streamly</div>
    <div class="social-row"><span class="social-dot"></span>chirpnet</div>
  </div>
  <div class="copyright">COPYRIGHT © 2018 BRACKENFIELDGOODS.COM. ALL RIGHTS RESERVED.</div>
</footer>

</body>
</html>
```